Larkfield Meadow Apiary Co.

Using the logo created by your designer I need to have a label made for retail sales of my product (Local Raw Honey) local and raw are the key phrases that would need to stand out to the consumer on the grocery shelves or farmers markets and that this is a 100% pure product. The label will also need to include Net weight in pounds and kg with space for me to write in the numerals as I have multiple size jars (I've included my home made label for reference on the Net weight requirements for my state) and I will need my business name and address "Larkfeld Meadow Apiary Co. 1837 Tallow Creek Rd SW North Larkfield Mi. 38514" at the bottom of the of the label.

```html
<!DOCTYPE html>
<html lang="en">
<head>
<meta charset="utf-8">
<title>Wren's Honey – Label</title>
<link href="https://fonts.googleapis.com/css2?family=Cormorant+Garamond:wght@600&family=Poppins:wght@500;600;900&display=swap" rel="stylesheet">
<style>
  :root {
    --backdrop: #d9d9d9;
    --paper: #ffffff;
    --honey: #a36a25;
    --comb-tint: #f3e7d6;
    --ink: #111111;
  }
  * { margin: 0; padding: 0; box-sizing: border-box; }
  html, body { width: 1200px; height: 1200px; overflow: hidden; }
  body { background: var(--backdrop); position: relative; font-family: "Poppins", sans-serif; color: var(--ink); }

  .label { position: absolute; left: 271px; width: 675px; height: 452px; background: var(--paper); overflow: hidden; }
  .label--front { top: 132px; }
  .label--back { top: 631px; }

  .comb { position: absolute; }
  .comb--top { left: 0; top: 0; width: 329px; height: 152px; }
  .comb--bottom { right: 0; bottom: 0; width: 329px; height: 152px; }

  .brand { position: absolute; left: 0; right: 0; top: 52px; text-align: center; }
  .brand__dot { display: block; width: 34px; height: 34px; border-radius: 50%; background: var(--honey); margin: 0 auto 10px; }
  .brand__name { font-family: "Poppins", sans-serif; font-weight: 600; font-size: 11px; letter-spacing: 0.12em; color: var(--honey); text-transform: uppercase; }

  .product-title { position: absolute; left: 0; right: 0; top: 170px; text-align: center; font-family: "Cormorant Garamond", serif; font-weight: 600; font-size: 64px; line-height: 1; color: var(--honey); letter-spacing: 0.01em; }
  .product-type { position: absolute; left: 0; right: 0; top: 252px; text-align: center; font-size: 13px; font-weight: 600; letter-spacing: 0.38em; }
  .accent-bar { position: absolute; left: 324px; top: 294px; width: 28px; height: 4px; background: var(--honey); }
  .tagline { position: absolute; left: 0; right: 0; top: 320px; text-align: center; font-size: 8px; font-weight: 600; letter-spacing: 0.32em; }
  .weight-line { position: absolute; left: 248px; top: 379px; width: 180px; height: 1px; background: var(--ink); }
  .net-weight { position: absolute; left: 248px; top: 394px; font-size: 10.5px; font-weight: 500; letter-spacing: 0.32em; white-space: nowrap; }

  .back-copy { position: absolute; left: 0; right: 0; top: 66px; text-align: center; font-size: 16px; line-height: 20.6px; font-weight: 500; letter-spacing: 0.32em; }
  .back-copy p { margin-bottom: 20.6px; }
  .back-copy strong { font-weight: 900; }
  .back-copy .made-in { font-weight: 900; }
</style>
</head>
<body>

<section class="label label--front">
  <svg class="comb comb--top" viewBox="0 0 329 152" role="img" aria-label="Honeycomb pattern in thin gold outlines">
    <polygon points="0,0 329,0 310,34 250,34 215,84 180,84 155,118 80,152 55,120 0,60" fill="var(--comb-tint)"/>
  </svg>
  <svg class="comb comb--bottom" viewBox="0 0 329 152" role="img" aria-label="Honeycomb pattern in thin gold outlines">
    <polygon points="329,152 0,152 0,120 20,100 100,66 150,34 200,0 260,16 300,66 329,84" fill="var(--comb-tint)"/>
  </svg>

  <div class="brand">
    <span class="brand__dot"></span>
    <div class="brand__name">Larkfield Meadow Apiary Co.</div>
  </div>

  <h1 class="product-title">WREN’S HONEY</h1>
  <div class="product-type">LOCAL RAW WILDFLOWER HONEY</div>
  <div class="accent-bar"></div>
  <div class="tagline">BROUGHT TO YOU BY LOCAL MICHIGAN BEE’S</div>
  <div class="weight-line"></div>
  <div class="net-weight">NET WT. 16 OZ (.45 kg)</div>
</section>

<section class="label label--back">
  <svg class="comb comb--top" viewBox="0 0 329 152" role="img" aria-label="Honeycomb pattern in thin gold outlines">
    <polygon points="0,0 329,0 310,34 250,34 215,84 180,84 155,118 80,152 55,120 0,60" fill="var(--comb-tint)"/>
  </svg>
  <svg class="comb comb--bottom" viewBox="0 0 329 152" role="img" aria-label="Honeycomb pattern in thin gold outlines">
    <polygon points="329,152 0,152 0,120 20,100 100,66 150,34 200,0 260,16 300,66 329,84" fill="var(--comb-tint)"/>
  </svg>

  <div class="back-copy">
    <p><strong>DISCLAIMER:</strong> PROCESSED IN A<br>FACILITY NOT INSPECTED BY THE<br>DEPARTMENT OF AGRICULTURE &amp;<br>RURAL DEVELOPMENT</p>
    <p>MINIMALLLY FILTERED</p>
    <p class="made-in">ALL PACKAGING PRODUCED IN<br>THE USA</p>
    <p>LARKFIELD MEADOW BEE CO.<br>1837 TALLOW CREEK RD SW NORTH<br>LARKFIELD MI 38514</p>
  </div>
</section>

</body>
</html>
```